Label for a bottle of Gin soon to launch in the UK.

We need a label for a gin called Marbury Gin. It is very important that the label does not infringe any copyrights of the football club so please avoid the colour blue or anything related to football or the club. The example bottle below shows the bottle that we will be using. The gin will be clear not pink, the use of gold on the label is encouraged.
Should not infringe on the brand shown in the example image.

Industry/Entity Type

Club

Font styles to use
Sans Serif

Requirements
Must have
• Here is a link to the bottle that the label must fit onto https://www.vessel-depot-example.co.uk/Glass-bottles/Glass-bottles/700ml-glass-bottles/700ml-clear-glass-bottle-Quilora.html
Should not have
• No use of blue or anything related to football or Halcombe Rowing Society or Stonewrens. Avoid Red also. White, gold and black should be primary colours used

```html
<!DOCTYPE html>
<html lang="en">
<head>
<meta charset="utf-8">
<title>Marbury Gin – Bottle Label</title>
<link rel="stylesheet" href="https://fonts.googleapis.com/css2?family=Teko:wght@600&family=Arimo:wght@700&display=swap">
<style>
  :root {
    --paper: #ffffff;
    --ink: #161616;
    --label-white: #ffffff;
    --gold: #e2b41c;
    --gold-light: #f7d63c;
    --gold-deep: #b88f14;
    --text-light: #ffffff;
  }
  html, body {
    margin: 0;
    padding: 0;
    width: 1200px;
    height: 1200px;
    overflow: hidden;
    background: var(--paper);
  }
  .canvas {
    width: 1200px;
    height: 1200px;
    display: flex;
    align-items: center;
    justify-content: center;
  }
  .label {
    width: 1100px;
    height: 906px;
    display: block;
  }
  .label-frame { fill: var(--ink); }
  .label-panel { fill: var(--label-white); }
  .label-title {
    font-family: "Teko", "Arial Narrow", sans-serif;
    font-weight: 600;
    font-size: 118px;
    fill: var(--gold);
    stroke: var(--ink);
    stroke-width: 3px;
    paint-order: stroke fill;
    letter-spacing: 2px;
  }
  .label-specs {
    font-family: "Arimo", Arial, sans-serif;
    font-weight: 700;
    font-size: 19px;
    fill: var(--text-light);
  }
  .gold-flag-start { stop-color: var(--gold-light); }
  .gold-flag-end { stop-color: var(--gold-deep); }
</style>
</head>
<body>
<main class="canvas">
  <svg class="label" viewBox="340 440 510 420" xmlns="http://www.w3.org/2000/svg" aria-label="Marbury Gin label">
    <defs>
      <linearGradient id="goldFlag" x1="0" y1="0" x2="1" y2="0">
        <stop offset="0" class="gold-flag-start"/>
        <stop offset="1" class="gold-flag-end"/>
      </linearGradient>
    </defs>

    <polygon class="gold-flag" fill="url(#goldFlag)" points="386,768 672,668 672,826"/>

    <g class="label-band" transform="translate(373 600) skewY(-17.1)">
      <rect class="label-frame" x="0" y="0" width="449" height="165"/>
      <rect class="label-panel" x="10" y="10" width="429" height="102"/>
      <text class="label-title" x="224.5" y="104" text-anchor="middle" textLength="408" lengthAdjust="spacingAndGlyphs">MARBURY GIN</text>
      <text class="label-specs" x="22" y="150" textLength="405" lengthAdjust="spacing" xml:space="preserve">47% Vol.   /   94 PROOF   /   70CL</text>
    </g>
  </svg>
</main>
</body>
</html>
```